3 point buck deer with toolbelt

I would like to have a logo that has a 3 point buck deer as a handyman/tuff guy with a tool belt on, flexing and holding a hammer.

Target Market(s)

homeowners

Industry/Entity Type

Handyman

Contact Information for Business Card

Ridgeway Builders; Dale R. Whitcomb; 4837 Marlow Ct., Alder Bend, WA 98990; 509.314.2768; ridgewaybuild@mailbox-demo.com

Font styles to use
Serif

Requirements
Must have
• a 3 point buck deer with a toolbelt
Nice to have
• hammer, broom, saw
Should not have
• the color pink

```html
<!DOCTYPE html>
<html lang="en">
<head>
<meta charset="utf-8">
<title>Ridgeway Builders – Business Card</title>
<link rel="stylesheet" href="https://fonts.googleapis.com/css2?family=Exo+2:wght@400;500&display=swap">
<style>
  :root {
    --stage: #050707;
    --teal: #62bfc4;
    --teal-light: #9dd9dc;
    --paper: #ffffff;
    --paper-tint: #f0fafc;
    --mark: #00c2cf;
    --title: #0d4f5c;
    --ink: #0c1214;
  }
  html, body {
    margin: 0;
    padding: 0;
    width: 1200px;
    height: 1000px;
    overflow: hidden;
    background: var(--stage);
  }
  .business-card {
    position: absolute;
    left: 79px;
    top: 193px;
    width: 1046px;
    height: 610px;
    background: var(--teal);
    overflow: hidden;
    font-family: "Exo 2", "Trebuchet MS", sans-serif;
  }
  .card-art {
    position: absolute;
    inset: 0;
  }
  .company-name {
    position: absolute;
    left: 58px;
    top: 216px;
    margin: 0;
    font-size: 40px;
    font-weight: 400;
    letter-spacing: 1px;
    color: var(--title);
    white-space: nowrap;
  }
  .brand-mark {
    position: absolute;
    left: 618px;
    top: 268px;
    display: flex;
    align-items: center;
    gap: 14px;
    white-space: nowrap;
  }
  .brand-mark-dot {
    width: 34px;
    height: 34px;
    border-radius: 50%;
    background: var(--mark);
  }
  .brand-mark-name {
    font-size: 30px;
    font-weight: 500;
    color: var(--mark);
  }
  .contact-block {
    position: absolute;
    left: 97px;
    top: 353px;
    margin: 0;
    font-size: 21px;
    line-height: 35.5px;
    color: var(--ink);
    text-transform: uppercase;
    font-style: normal;
  }
  .contact-email {
    position: absolute;
    left: 446px;
    top: 518px;
    font-size: 20px;
    color: var(--ink);
    white-space: nowrap;
  }
</style>
</head>
<body>
  <section class="business-card">
    <svg class="card-art" width="1046" height="610" viewBox="0 0 1046 610" xmlns="http://www.w3.org/2000/svg" aria-hidden="true">
      <defs>
        <linearGradient id="paperGradient" x1="0" y1="0" x2="1" y2="1">
          <stop offset="0" stop-color="#ffffff"/>
          <stop offset="0.6" stop-color="#f0fafc"/>
          <stop offset="1" stop-color="#ffffff"/>
        </linearGradient>
      </defs>
      <path class="wave-band" fill="#9dd9dc" transform="translate(-30,0)"
        d="M388,0 L1076,0 L1076,610 L888,610 C860,540 820,500 700,480 C560,450 510,410 520,330 C530,270 590,250 580,210 C570,175 510,172 420,170 C350,165 340,120 360,60 Z"/>
      <path class="wave-paper" fill="url(#paperGradient)"
        d="M388,0 L1046,0 L1046,610 L888,610 C860,540 820,500 700,480 C560,450 510,410 520,330 C530,270 590,250 580,210 C570,175 510,172 420,170 C350,165 340,120 360,60 Z"/>
    </svg>

    <h1 class="company-name">RIDGEWAY BUILDERS</h1>

    <div class="brand-mark">
      <span class="brand-mark-dot"></span>
      <span class="brand-mark-name">Ridgeway Builders</span>
    </div>

    <address class="contact-block">
      Dale R. Whitcomb<br>
      4837 Marlow Ct<br>
      Alder Bend<br>
      WA 98990<br>
      509.314.2768
    </address>
    <div class="contact-email">ridgewaybuild@mailbox-demo.com</div>
  </section>
</body>
</html>
```